Upscale business cards needed for family business

We need professional business cards created for several family members. We are a family business holding company. We would like these relatively simple and straightforward, but also with a unique element to set them apart. Probably stick with neutral and simple colors - white, grey etc. We need space for the traditional elements, including name, title, address, email/phone number. And we will be creating several from this template so it needs to be template that is easy to switch information in and out of.

Industry/Entity Type

Business

Contact Information for Business Card

Please include the attached Marwood Capital logo.

Requirements
Must have
• The attached Marwood Capital logo.

```html
<!DOCTYPE html>
<html lang="en">
<head>
<meta charset="utf-8">
<title>Marwood Capital – Business Card</title>
<link href="https://fonts.googleapis.com/css2?family=Playfair+Display:wght@400;700&family=Lato:wght@400&family=Cinzel:wght@400&display=swap" rel="stylesheet">
<style>
  :root {
    --page-bg: #e4e5e8;
    --card-bg: #ffffff;
    --ink: #111111;
    --ink-deep: #000000;
    --band: #1f1816;
    --text: #1c1c1c;
    --brand-text: #ffffff;
  }
  * { margin: 0; padding: 0; box-sizing: border-box; }
  html, body {
    width: 1200px; height: 800px; overflow: hidden;
    background: var(--page-bg);
  }
  .canvas {
    position: relative; width: 1200px; height: 800px;
    display: flex; align-items: center; justify-content: center;
  }
  .card {
    position: relative; width: 1050px; height: 600px;
    background: var(--card-bg); overflow: hidden;
    box-shadow: 0 10px 30px rgba(0,0,0,0.12);
  }
  .card-shapes { position: absolute; inset: 0; }
  .brand {
    position: absolute; left: 150px; top: 215px; width: 250px;
    text-align: center;
    font-family: "Cinzel", serif; font-weight: 400;
    font-size: 24px; letter-spacing: 1px;
    color: var(--brand-text);
  }
  .identity { position: absolute; left: 560px; top: 195px; }
  .identity-name {
    font-family: "Playfair Display", serif; font-weight: 700;
    font-size: 60px; line-height: 1; color: var(--ink);
  }
  .identity-title {
    font-family: "Playfair Display", serif; font-weight: 400;
    font-size: 32px; color: var(--text); margin-top: 2px;
  }
  .identity-rule {
    width: 70px; height: 3px; background: var(--ink); margin-top: 6px;
  }
  .contact-list {
    position: absolute; left: 560px; top: 370px;
    list-style: none;
    font-family: "Lato", sans-serif; font-size: 26px; color: var(--text);
  }
  .contact-item {
    display: flex; align-items: flex-start; gap: 18px; margin-bottom: 20px;
    line-height: 1.25;
  }
  .contact-icon { width: 38px; height: 38px; flex: none; }
</style>
</head>
<body>
<div class="canvas">
  <div class="card">
    <svg class="card-shapes" width="1050" height="600" viewBox="0 0 1050 600" aria-hidden="true">
      <circle cx="-120" cy="120" r="560" fill="var(--band)"/>
      <circle cx="90" cy="120" r="380" fill="var(--ink-deep)" stroke="#ffffff" stroke-width="3"/>
    </svg>

    <div class="brand">MARWOOD CAPITAL</div>

    <div class="identity">
      <div class="identity-name">Name</div>
      <div class="identity-title">Title of the person</div>
      <div class="identity-rule"></div>
    </div>

    <ul class="contact-list">
      <li class="contact-item">
        <svg class="contact-icon" viewBox="0 0 38 38" aria-label="Phone">
          <circle cx="19" cy="19" r="19" fill="var(--ink)"/>
          <path d="M13 10c1-1 2-1 3 0l2 3c.6 1 .4 1.8-.4 2.5l-1 .8c.8 2 2.5 3.8 4.6 4.6l.8-1c.7-.8 1.6-1 2.5-.4l3 2c1 1 1 2 0 3l-1.5 1.5c-4 1-13-8-12-12z" fill="#fff"/>
        </svg>
        <span>700-800-7000</span>
      </li>
      <li class="contact-item">
        <svg class="contact-icon" viewBox="0 0 38 38" aria-label="Email">
          <circle cx="19" cy="19" r="19" fill="var(--ink)"/>
          <rect x="10" y="13" width="18" height="12" fill="#fff"/>
          <path d="M10 13l9 7 9-7" fill="none" stroke="var(--ink)" stroke-width="1.5"/>
        </svg>
        <span>forexample@example.com</span>
      </li>
      <li class="contact-item">
        <svg class="contact-icon" viewBox="0 0 38 38" aria-label="Address">
          <circle cx="19" cy="19" r="19" fill="var(--ink)"/>
          <path d="M19 8a7 7 0 0 0-7 7c0 5 7 14 7 14s7-9 7-14a7 7 0 0 0-7-7z" fill="#fff"/>
          <circle cx="19" cy="15" r="2.6" fill="var(--ink)"/>
        </svg>
        <span>for example 77 example st,<br>suite 7 family.</span>
      </li>
    </ul>
  </div>
</div>
</body>
</html>
```